Brightfold

New company offering Accounting and bookkeeping for small and medium business in Cayman Islands. please see content on my website. www.brightfold.ky or www.brightfold-accountants.co.uk

Industry/Entity Type

Accounting

Requirements
Must have
• Simple, clean design
Should not have
• clutter

```html
<!DOCTYPE html>
<html lang="en">
<head>
<meta charset="utf-8">
<title>Brightfold Accountants – Your Partner for Successful Growth</title>
<link rel="stylesheet" href="https://fonts.googleapis.com/css2?family=Oswald:wght@500;700&family=Open+Sans:wght@400;600;700&display=swap">
<style>
:root{
  --navy:#1c3656;
  --navy-dark:#142a45;
  --green:#7cbf3f;
  --paper:#eef0f2;
  --ink:#2b2f36;
  --rule:#b9c2cc;
  --white:#ffffff;
}
*{margin:0;padding:0;box-sizing:border-box}
html,body{width:857px;height:1200px;overflow:hidden;background:var(--paper)}
body{font-family:"Open Sans",Arial,sans-serif;color:var(--ink);position:relative}
.banner{height:108px;background:var(--navy);border-bottom:5px solid var(--green);display:flex;align-items:center;justify-content:center}
.banner h1{font-family:"Oswald",Arial,sans-serif;font-weight:700;color:var(--white);font-size:40px;letter-spacing:1px}
.services{display:grid;grid-template-columns:1fr 1fr;column-gap:40px;padding:34px 34px 0;row-gap:26px}
.service-head{display:flex;align-items:center;gap:12px;border-bottom:2px solid var(--rule);padding-bottom:8px;margin-bottom:12px}
.service-icon{width:44px;height:44px;border-radius:50%;background:var(--green);display:flex;align-items:center;justify-content:center;flex:none}
.service-head h2{font-family:"Oswald",Arial,sans-serif;font-weight:500;color:var(--navy);font-size:25px;letter-spacing:.5px;text-transform:uppercase}
.service-list{list-style:none;font-size:14.2px;line-height:1.62}
.service-list li{padding-left:16px;position:relative}
.service-list li::before{content:"";position:absolute;left:2px;top:9px;width:6px;height:6px;border-radius:50%;background:var(--navy)}
.service-text{font-size:14.2px;line-height:1.5}
.brand{position:absolute;left:0;right:0;top:1000px;display:flex;align-items:center;justify-content:center;gap:16px}
.brand-dot{width:46px;height:46px;border-radius:50%;background:var(--green)}
.brand-name{font-family:"Oswald",Arial,sans-serif;font-weight:700;font-size:46px;color:var(--navy);letter-spacing:2px;text-transform:uppercase;line-height:1}
.contact-bar{position:absolute;left:0;right:0;bottom:0;height:76px;background:var(--navy);border-top:5px solid var(--green);display:flex;align-items:center;justify-content:space-around;padding:0 20px;color:var(--white);font-size:13px}
.contact-item{display:flex;align-items:center;gap:7px}
.contact-item svg{flex:none}
</style>
</head>
<body>
<header class="banner"><h1>YOUR PARTNER FOR SUCCESSFUL GROWTH</h1></header>

<main class="services">
  <section class="service">
    <div class="service-head">
      <span class="service-icon"><svg width="24" height="24" viewBox="0 0 24 24" fill="none" stroke="#fff" stroke-width="2"><path d="M4 4h11a3 3 0 0 1 3 3v13H7a3 3 0 0 1-3-3z"/><path d="M8 9h6M8 13h6"/></svg></span>
      <h2>Bookkeeping</h2>
    </div>
    <ul class="service-list">
      <li>Preparation and processing of sales invoices</li>
      <li>Posting and allocation of deposits</li>
      <li>Credit control</li>
      <li>Processing, coding and posting of supplier invoices</li>
      <li>Posting and allocation of supplier direct debit payments</li>
      <li>Production of cheques in accordance with credit terms</li>
      <li>Posting and allocation of supplier payments</li>
      <li>Analyzing and posting of petty cash payments</li>
      <li>Payroll journal entries</li>
      <li>Depreciation journals</li>
      <li>Interest journals</li>
      <li>Accruals and prepayments</li>
      <li>Bank and credit card reconciliations</li>
    </ul>
  </section>

  <section class="service">
    <div class="service-head">
      <span class="service-icon"><svg width="24" height="24" viewBox="0 0 24 24" fill="#fff"><rect x="4" y="13" width="4" height="7"/><rect x="10" y="8" width="4" height="12"/><rect x="16" y="4" width="4" height="16"/></svg></span>
      <h2>Management Accounts</h2>
    </div>
    <p class="service-text">Management accounts are what they say they are. Accounts which are prepared with the aim of helping managers make important business decisions, whilst having the benefit of full financial information. Many small businesses rely solely on the end of year accounts to understand their financial situation and as a result probably miss a number of opportunities or make bad decisions, simply because they did not have access to accurate, timely, financial information. Management accounts can be produced monthly, quarterly, half-yearly or any other period that is relevant to you. Dashboards are a popular method of displaying financial information in an easy to understand format. We will work with you to understand what key figures drives the performance of your business and then present them in an easy to understand format - for example charts and graphs. This allows for quick decision making for fast growing and entrepreneurial businesses.</p>
  </section>

  <section class="service">
    <div class="service-head">
      <span class="service-icon"><svg width="24" height="24" viewBox="0 0 24 24" fill="none" stroke="#fff" stroke-width="2"><circle cx="12" cy="12" r="8"/><path d="M14.5 9.2c-.6-.8-1.5-1.2-2.5-1.2-1.4 0-2.5.8-2.5 2s1.1 1.6 2.5 2 2.5.8 2.5 2-1.1 2-2.5 2c-1 0-1.9-.4-2.5-1.2M12 6.5v11"/></svg></span>
      <h2>Payroll</h2>
    </div>
    <ul class="service-list">
      <li>Total flexibility with unlimited pay types</li>
      <li>Healthcare and Pension calculations</li>
      <li>Extremely cost effective rates</li>
      <li>No payroll knowledge is required by the client</li>
      <li>Accurate employee records, constantly maintained</li>
      <li>Dedicated, experienced payroll experts, providing peace of mind</li>
      <li>Hassle free process - just 'fill in the blanks' and we will expedite the salary information to you</li>
      <li>PDF Payslips emailed to person email addresses to ensure staff security is guaranteed</li>
      <li>Monthly payroll reports</li>
    </ul>
  </section>

  <section class="service">
    <div class="service-head">
      <span class="service-icon"><svg width="24" height="24" viewBox="0 0 24 24" fill="none" stroke="#fff" stroke-width="2"><circle cx="12" cy="12" r="3"/><path d="M12 3v3M12 18v3M3 12h3M18 12h3M5.6 5.6l2.1 2.1M16.3 16.3l2.1 2.1M5.6 18.4l2.1-2.1M16.3 7.7l2.1-2.1"/></svg></span>
      <h2>Other Services</h2>
    </div>
    <ul class="service-list">
      <li>Bring past accounts up to date</li>
      <li>Address delinquent pension accounts</li>
      <li>Business Plans</li>
      <li>Financial Modelling</li>
      <li>Budget and Forecasting</li>
      <li>Cash flow Analysis</li>
      <li>Profitability Analysis</li>
    </ul>
  </section>
</main>

<div class="brand">
  <span class="brand-dot"></span>
  <span class="brand-name">Brightfold Accountants</span>
</div>

<footer class="contact-bar">
  <span class="contact-item"><svg width="16" height="16" viewBox="0 0 24 24" fill="#7cbf3f"><path d="M6.6 10.8a15 15 0 0 0 6.6 6.6l2.2-2.2a1 1 0 0 1 1-.25 11 11 0 0 0 3.6.6 1 1 0 0 1 1 1V20a1 1 0 0 1-1 1A17 17 0 0 1 3 4a1 1 0 0 1 1-1h3.5a1 1 0 0 1 1 1 11 11 0 0 0 .6 3.6 1 1 0 0 1-.25 1z"/></svg>(345) 5550147</span>
  <span class="contact-item"><svg width="14" height="18" viewBox="0 0 24 30" fill="#7cbf3f"><path d="M12 0a10 10 0 0 0-10 10c0 7.5 10 20 10 20s10-12.5 10-20A10 10 0 0 0 12 0zm0 14a4 4 0 1 1 0-8 4 4 0 0 1 0 8z"/></svg>Harbour Court PO Box 40110 Grand Cayman KY1-1300</span>
  <span class="contact-item"><svg width="18" height="14" viewBox="0 0 24 18" fill="none" stroke="#7cbf3f" stroke-width="2"><rect x="1" y="1" width="22" height="16" rx="2"/><path d="M1 2l11 8 11-8"/></svg>info@brightfold.ky</span>
  <span class="contact-item"><svg width="16" height="16" viewBox="0 0 24 24" fill="none" stroke="#7cbf3f" stroke-width="2"><circle cx="12" cy="12" r="10"/><path d="M2 12h20M12 2c3 3 3 17 0 20M12 2c-3 3-3 17 0 20"/></svg>www.brightfold.ky</span>
</footer>
</body>
</html>
```